Save our Business Card - We need your help

We need a fresh look on our business cards. We like it as it is, but it's not quite getting the 'wow' effect that we desire.
We're a tech startup building a cloud based solution for retailers consisting of Point of Sale, Inventory management and CRM.
The design should communicate a sense of a company that cares about the little things, design and relationships.
You can have a look at our website www.brimvale.com to get a feel for what we're like. Please feel free to message us for any further clarification
Our Customers are retail busines owners, cafe owners, other startups etc.
Building

```html
<!DOCTYPE html>
<html lang="en">
<head>
<meta charset="utf-8">
<title>Brimvale Business Card</title>
<link rel="stylesheet" href="https://fonts.googleapis.com/css2?family=Ubuntu:wght@400;500&display=swap">
<style>
  :root {
    --stage: #2a2a2b;
    --card-dark: #3b3b3d;
    --pattern: #4a4a4c;
    --orange: #f29223;
    --ink: #3a3a3a;
    --ink-soft: #4d4d4d;
    --white: #ffffff;
  }
  * { margin: 0; padding: 0; box-sizing: border-box; }
  html, body { width: 1200px; height: 900px; overflow: hidden; }
  body {
    background: var(--stage);
    font-family: "Ubuntu", Arial, sans-serif;
    position: relative;
  }
  .card {
    position: absolute;
    top: 302px;
    width: 513px;
    height: 296px;
    overflow: hidden;
  }
  .card-back { left: 73px; background: var(--card-dark); }
  .card-front { left: 615px; background: var(--white); }

  .back-pattern {
    position: absolute; inset: 0;
    background: linear-gradient(135deg, var(--card-dark), var(--pattern) 50%, var(--card-dark));
    opacity: .6;
  }
  .back-brand {
    position: absolute;
    left: 362px; top: 188px;
    display: flex; align-items: center; gap: 8px;
  }
  .back-brand .mark { width: 22px; height: 22px; background: var(--orange); }
  .back-brand .name { color: var(--white); font-size: 20px; font-weight: 500; }

  .front-swoosh { position: absolute; inset: 0; width: 513px; height: 296px; }
  .holder {
    position: absolute; left: 34px; top: 31px; color: var(--white);
  }
  .holder .person { font-size: 17px; font-weight: 400; line-height: 20px; }
  .holder .role { font-size: 13px; line-height: 16px; }

  .front-brand {
    position: absolute; right: 34px; top: 78px;
    display: flex; align-items: center; gap: 10px;
  }
  .front-brand .mark { width: 34px; height: 34px; background: var(--orange); }
  .front-brand .name { color: var(--orange); font-size: 29px; font-weight: 500; }

  .contacts {
    position: absolute; left: 66px; top: 198px; list-style: none;
  }
  .contacts li {
    display: flex; align-items: center; gap: 9px;
    height: 20px; font-size: 13px; color: var(--ink);
  }
  .contacts svg { width: 11px; height: 11px; fill: var(--orange); flex: none; }

  .address {
    position: absolute; right: 34px; top: 199px;
    text-align: right; font-style: normal;
    font-size: 11.5px; line-height: 15.6px; color: var(--ink-soft);
  }
</style>
</head>
<body>
  <section class="card card-back" aria-label="Card back">
    <div class="back-pattern" role="img" aria-label="Repeating pattern of faint brand motifs"></div>
    <div class="back-brand">
      <span class="mark"></span>
      <span class="name">Brimvale</span>
    </div>
  </section>

  <section class="card card-front" aria-label="Card front">
    <svg class="front-swoosh" viewBox="0 0 513 296" aria-hidden="true">
      <path d="M0,0 H356 C250,40 60,140 0,268 Z" fill="var(--orange)"/>
      <path d="M376,0 H412 C300,22 70,130 0,286 L0,278 C62,138 268,26 376,0 Z" fill="var(--ink)"/>
    </svg>

    <div class="holder">
      <p class="person">Daniel Okafor</p>
      <p class="role">managing director</p>
    </div>

    <div class="front-brand">
      <span class="mark"></span>
      <span class="name">Brimvale</span>
    </div>

    <ul class="contacts">
      <li>
        <svg viewBox="0 0 12 12"><path d="M2.5 1 L4.5 1 L5.3 3.5 L4 4.6 C4.7 6 6 7.3 7.4 8 L8.5 6.7 L11 7.5 L11 9.5 C11 10.4 10.3 11 9.5 11 C5 11 1 7 1 2.5 C1 1.7 1.6 1 2.5 1 Z"/></svg>
        555 214 37 90
      </li>
      <li>
        <svg viewBox="0 0 12 12"><path d="M3.5 0.5 H8.5 A1 1 0 0 1 9.5 1.5 V10.5 A1 1 0 0 1 8.5 11.5 H3.5 A1 1 0 0 1 2.5 10.5 V1.5 A1 1 0 0 1 3.5 0.5 Z M4 2 V9 H8 V2 Z"/></svg>
        888 406 21 53
      </li>
      <li>
        <svg viewBox="0 0 12 12"><path d="M0.5 2.5 H11.5 V3.2 L6 6.6 L0.5 3.2 Z M0.5 4.4 L6 7.8 L11.5 4.4 V9.5 H0.5 Z"/></svg>
        support@brimvale.com
      </li>
      <li>
        <svg viewBox="0 0 12 12"><path d="M6 0.5 A5.5 5.5 0 1 0 6 11.5 A5.5 5.5 0 1 0 6 0.5 Z M6 1.6 C5 2.6 4.5 4 4.4 5.4 H7.6 C7.5 4 7 2.6 6 1.6 Z M1.7 5.4 H3.4 C3.5 4 3.9 2.8 4.5 1.9 C3 2.4 1.9 3.8 1.7 5.4 Z M8.6 5.4 H10.3 C10.1 3.8 9 2.4 7.5 1.9 C8.1 2.8 8.5 4 8.6 5.4 Z M1.7 6.6 C1.9 8.2 3 9.6 4.5 10.1 C3.9 9.2 3.5 8 3.4 6.6 Z M4.4 6.6 C4.5 8 5 9.4 6 10.4 C7 9.4 7.5 8 7.6 6.6 Z M8.6 6.6 C8.5 8 8.1 9.2 7.5 10.1 C9 9.6 10.1 8.2 10.3 6.6 Z"/></svg>
        www.brimvale.com
      </li>
    </ul>

    <address class="address">
      Unit B-3-12, Block B<br>
      24 Riverside Walk<br>
      Jalan Harmoni 4<br>
      50480 Kuala Lumpur<br>
      Wilayah, Malaysia
    </address>
  </section>
</body>
</html>
```